Harbour Green Rink Events - Flyer

So now that i have the logo, I need a flyer made up for printing to be delivered to businesses and residential homes.
Below is some information that I want included in the design, in any order and in anyway.
What better way to spend time with family, friends or workmates then to enjoy 2 hours of barefoot bowls.
We can cater for Xmas Parties, Buck's and Hen's Parties, Birthday Parties, Team Building events.
We have food and drink packages to suit all your needs.
So why not come along and have the best fun you can have on 2 feet!
We have 2 locations at Wattlebrook Sports and Bowling Club and Merriden Bowling Club
Prices start from $12pp for 2 hours of lawn bowls fun
Contact Wade Kessler on 0482 157 394 or visit our website www.harbourgreenrinkevents.com.au for more information and to enquire about your function today!

```html
<!DOCTYPE html>
<html lang="en">
<head>
<meta charset="utf-8">
<title>Barefoot Lawnbowls – Harbour Green Rink Events</title>
<link rel="stylesheet" href="https://fonts.googleapis.com/css2?family=Arimo:wght@400;700&family=Questrial&display=swap">
<style>
  :root {
    --ink: #3b3b3b;
    --text: #4a4a4a;
    --label: #222222;
    --red: #d6282b;
    --forest: #0c2d26;
    --teal: #1db08c;
    --white: #ffffff;
    --turf-light: #8cbc55;
    --turf-dark: #5e9838;
  }
  * { margin: 0; padding: 0; box-sizing: border-box; }
  html, body { width: 1200px; height: 846px; overflow: hidden; background: var(--white); }
  .flyer {
    position: relative; width: 1200px; height: 846px;
    font-family: "Arimo", Arial, sans-serif; color: var(--text); overflow: hidden;
  }
  .headline {
    position: absolute; right: 14px; top: 2px;
    font-weight: 700; font-size: 82px; letter-spacing: 0.5px; color: var(--ink);
    white-space: nowrap;
  }
  .panel { position: absolute; }
  .panel svg { display: block; }
  .panel-intro { left: 655px; top: 108px; width: 545px; height: 182px; }
  .intro-copy {
    position: absolute; left: 708px; top: 116px; width: 450px;
    color: var(--white); font-size: 24px; line-height: 33px;
  }
  .price-box {
    position: absolute; left: 733px; top: 218px; width: 374px; height: 65px;
    background: var(--white); color: var(--red); padding: 8px 0 0 32px;
    font-size: 20px; line-height: 27px;
  }
  .price-box strong { font-size: 22px; }
  .cater-label {
    position: absolute; left: 10px; top: 142px;
    font-family: "Questrial", sans-serif; font-weight: 400; font-size: 39px; color: var(--label);
    white-space: nowrap;
  }
  .cater-list {
    position: absolute; left: 351px; top: 153px; width: 302px;
    font-size: 23px; line-height: 31.5px; color: var(--text);
  }
  .cater-list .accent { color: var(--red); }
  .hero {
    position: absolute; left: 0; top: 290px; width: 1200px; height: 370px;
    background: linear-gradient(180deg, var(--turf-light), var(--turf-dark));
  }
  .packages {
    position: absolute; left: 12px; top: 684px; font-size: 20px; color: var(--text);
    white-space: nowrap;
  }
  .packages b { font-family: "Questrial", sans-serif; font-weight: 400; font-size: 23px; color: var(--label); }
  .locations {
    position: absolute; left: 0; top: 730px; width: 525px; height: 103px;
    background: var(--red); color: var(--white);
  }
  .locations-label {
    position: absolute; left: 18px; top: 28px;
    font-family: "Questrial", sans-serif; font-weight: 400; font-size: 42px;
  }
  .locations-list {
    position: absolute; left: 213px; top: 8px; font-size: 24px; line-height: 31.5px;
  }
  .panel-contact { left: 518px; top: 660px; width: 682px; height: 186px; }
  .contact-title {
    position: absolute; left: 780px; top: 672px;
    font-family: "Questrial", sans-serif; font-weight: 400; font-size: 42px; color: var(--white);
  }
  .contact-lines {
    position: absolute; left: 696px; top: 731px;
    color: var(--white); font-size: 24px; line-height: 32px;
  }
  .contact-note {
    position: absolute; left: 595px; top: 808px; color: var(--white); font-size: 19.5px;
    white-space: nowrap;
  }
</style>
</head>
<body>
<main class="flyer">
  <h1 class="headline">Barefoot Lawnbowls</h1>

  <div class="panel panel-intro">
    <svg width="545" height="182" viewBox="0 0 545 182" aria-hidden="true">
      <path d="M5 0 Q24 90 26 182 L545 182 L545 0 Z" fill="var(--teal)"/>
      <path d="M17 0 Q36 90 36 182 L545 182 L545 0 Z" fill="var(--forest)"/>
    </svg>
  </div>
  <p class="intro-copy">What better way to spend time with family, friends or workmates then to enjoy 2 hours of barefoot bowls.</p>
  <p class="price-box"><strong>Prices:</strong> start from $12pp for<br>2 hours of lawn bowls fun</p>

  <h2 class="cater-label">We can cater for:</h2>
  <p class="cater-list">Xmas Parties, <span class="accent">Buck's and Hen's Parties</span>, Birthday Parties, <span class="accent">Team Building events.</span></p>

  <div class="hero" role="img" aria-label="Photo of barefoot players crouching on a bowling green, rolling lawn bowls"></div>

  <p class="packages"><b>We have</b>&nbsp; food and drink packages to suit all your needs.</p>

  <section class="locations">
    <h2 class="locations-label">locations:</h2>
    <p class="locations-list">Wattlebrook Sports and<br>Bowling Club and<br>Merriden Bowling Club</p>
  </section>

  <div class="panel panel-contact">
    <svg width="682" height="186" viewBox="0 0 682 186" aria-hidden="true">
      <path d="M118 0 Q80 110 0 186 L682 186 L682 0 Z" fill="var(--teal)"/>
      <path d="M128 0 Q92 110 14 186 L682 186 L682 0 Z" fill="var(--forest)"/>
    </svg>
  </div>
  <h2 class="contact-title">Contacts</h2>
  <p class="contact-lines">Wade Kessler:Tel 0482 157 394<br>www.harbourgreenrinkevents.com.au</p>
  <p class="contact-note">for more information and to enquire about your function today!</p>
</main>
</body>
</html>
```